Law Enforcement Non profit needs Trifold Brochure

We need a tri-fold brochure to advertise and explain what we do as an organization. Law enforcement colors are typically blue and black. Symbols are the Thin Blue Line, sirens, police cars,etc for our group they spray painted blue rose is one our groups recognizable symbols. We are also open to stock photo ideas. Our website is www.harborlanternfund.org The final design should motivate people to be interested in joining, giving a donation, or a better understanding of our group's goals. Files will include photo ideas we have, content, and we may need a final edit on the master design before the brochure is complete.

Target Market(s)

Local businesses in Minnesota and law enforcement

Industry/Entity Type

Non Profit

Font styles to use
Serif

Colors
2d73b3
3176b5
85abd2
3aa7d7
32a6d6
6dbee2

Requirements
Must have
• A dynamic look, trifold brochure. We would like a bold custom look...not looking like a generic template. I have included narratives and some optional photos but we are open on image design. standard size 8.5x11, layout in files section
Nice to have
• blue color scheme or police themed
Should not have
• a basic template look.

```html
<!DOCTYPE html>
<html lang="en">
<head>
<meta charset="utf-8">
<title>Harbor Lantern Fund – Trifold Brochure</title>
<link rel="stylesheet" href="https://fonts.googleapis.com/css2?family=Playfair+Display:wght@700&family=Nunito+Sans:wght@300;400&display=swap">
<style>
  :root {
    --navy: #2a2d86;
    --white: #ffffff;
    --ink: #1f1f24;
    --paper-grey: #eeeef1;
    --rule-light: rgba(255,255,255,0.55);
    --rule-dark: rgba(42,45,134,0.75);
  }
  * { box-sizing: border-box; margin: 0; padding: 0; }
  html, body { width: 1200px; height: 927px; overflow: hidden; background: var(--white); }
  .brochure { position: relative; width: 1200px; height: 927px; overflow: hidden; font-family: "Nunito Sans", sans-serif; font-weight: 300; }
  .panel { position: absolute; top: 0; width: 400px; height: 927px; }
  .panel--about { left: 0; background: var(--navy); color: var(--white); }
  .panel--join { left: 400px; background: var(--white); color: var(--ink); }
  .panel--community { left: 800px; background: linear-gradient(90deg, var(--paper-grey) 0%, var(--white) 14%); color: var(--ink); }

  .panel-title { position: absolute; top: 38px; left: 0; width: 400px; text-align: center; font-family: "Playfair Display", serif; font-weight: 700; font-size: 28px; line-height: 1; }
  .panel--about .panel-title { color: var(--white); }
  .panel--join .panel-title, .panel--community .panel-title { color: var(--navy); }
  .title-rule { position: absolute; top: 75px; left: 75px; width: 250px; height: 2px; }
  .panel--about .title-rule { background: linear-gradient(90deg, transparent, var(--rule-light), transparent); }
  .panel--join .title-rule, .panel--community .title-rule { background: linear-gradient(90deg, transparent, var(--rule-dark), transparent); }

  .photo { position: absolute; }
  .body-copy { position: absolute; font-size: 16px; line-height: 18.2px; white-space: nowrap; letter-spacing: -0.1px; }
  .body-copy p + p { margin-top: 11px; }
  .tight { letter-spacing: -0.55px; }
  .serif-strong { font-family: "Playfair Display", serif; font-weight: 700; font-size: 15px; letter-spacing: -0.2px; }

  .bullet-list { position: absolute; list-style: none; font-size: 16.5px; white-space: nowrap; }
  .bullet-list li { height: 27.2px; line-height: 27.2px; display: flex; align-items: center; }
  .bullet-list li::before { content: ""; width: 9px; height: 9px; border-radius: 50%; background: currentColor; margin-right: 6px; flex: none; }

  .support-shape { position: absolute; left: 0; top: 0; width: 1200px; height: 927px; pointer-events: none; }
  .support { position: absolute; left: 800px; top: 0; width: 400px; height: 927px; color: var(--white); }
  .support-title { position: absolute; top: 617px; left: 200px; width: 0; white-space: nowrap; display: flex; justify-content: center; font-family: "Playfair Display", serif; font-weight: 700; font-size: 28px; }
  .support-rule { position: absolute; top: 653px; left: 80px; width: 245px; height: 2px; background: linear-gradient(90deg, transparent, var(--rule-light), transparent); }
</style>
</head>
<body>
<main class="brochure">

  <section class="panel panel--about">
    <h2 class="panel-title">Who we are</h2>
    <div class="title-rule"></div>
    <div class="photo" role="img" aria-label="Group photo of members in matching navy t-shirts in an autumn forest" style="left:36px;top:96px;width:332px;height:181px;background:linear-gradient(160deg,#6f6a3a 0%,#3c3f6e 45%,#2e3560 70%,#5a4a30 100%);"></div>
    <div class="body-copy" style="left:35px;top:290px;">
      <p>Harbor Lantern Fund Inc. (HLF) is a locally<br>
      founded 501(c)(3) non-profit organization<br>
      dedicated to the support of the law<br>
      enforcement community in Minnesota.<br>
      Recognizing a need for a safe place for police<br>
      wives and families to share ideas, concerns,<br>
      faith, fitness and community, Dana Holloway<br>
      <span class="tight">founded Harbor Lantern Fund Inc in 2011. HLF</span><br>
      <span class="tight">provides a private online forum for communication</span><br>
      <span class="tight">as well as a number of committees to serve the law</span><br>
      <span class="tight">enforcement community:</span></p>
    </div>
    <ul class="bullet-list" style="left:56px;top:497px;">
      <li>Injured Officer</li>
      <li>Fallen Officer Memorial Rose</li>
      <li>Fundraising</li>
      <li>Membership</li>
      <li>Lantern Light Ball</li>
      <li>Social Events</li>
      <li>Marketing</li>
    </ul>
    <div class="photo" role="img" aria-label="Women in evening gowns raising blue cocktails in a toast at a gala" style="left:36px;top:700px;width:332px;height:197px;background:linear-gradient(170deg,#8a7560 0%,#4b3a33 45%,#2b2630 100%);"></div>
  </section>

  <section class="panel panel--join">
    <h2 class="panel-title">How to join</h2>
    <div class="title-rule"></div>
    <div class="body-copy" style="left:39px;top:102px;">
      <p>For female MN law enforcement significant<br>others:</p>
      <p>Potential members must submit a request<br>
      to join our private Circlebook page<br>
      <span class="serif-strong">(https://www.circlebook.com/groups/</span><br>
      <span class="serif-strong">harborlanternhome/)</span> and/or emailing our<br>
      membership chair at hlfmembership@<br>
      <span class="tight">harbormail.com. Requests will be contacted to</span><br>
      verify your information and approve your<br>
      request.&nbsp; You must be married or in a long<br>
      term committed relationship to join our<br>
      private page.&nbsp; Additional information and<br>
      applications can be found on our website.</p>
    </div>
    <div class="photo" role="img" aria-label="Gala floor projection announcing the Lantern Light Ball with a dancing couple" style="left:36px;top:368px;width:330px;height:244px;background:radial-gradient(ellipse at 50% 50%,#6a5a45 0%,#3a3128 60%,#221d19 100%);"></div>
    <div class="photo" role="img" aria-label="Runner with a child at a charity road race" style="left:36px;top:622px;width:143px;height:276px;background:linear-gradient(180deg,#c9ccd0 0%,#7f8b6a 35%,#3a3a40 65%,#6f6f72 100%);"></div>
    <div class="photo" role="img" aria-label="Honor guard officers in dress uniform beside flags" style="left:189px;top:622px;width:177px;height:276px;background:linear-gradient(120deg,#8a6b4e 0%,#2b2e45 40%,#14151d 75%,#3b3a40 100%);"></div>
  </section>

  <section class="panel panel--community">
    <h2 class="panel-title">For community supporters</h2>
    <div class="title-rule"></div>
    <div class="body-copy" style="left:42px;top:102px;">
      <p>We have a public Circlebook page that all<br>
      community supporters are welcome to<br>
      follow and share <span class="serif-strong">(@HarborLanternFund).</span></p>
    </div>
    <div class="photo" role="img" aria-label="Banquet table with flowers in a blue vase, glasses and desserts" style="left:36px;top:170px;width:332px;height:199px;background:linear-gradient(160deg,#b8a27a 0%,#6d6b6a 40%,#2c2c36 75%,#c8c6c2 100%);"></div>
    <div class="photo" role="img" aria-label="Volunteers handing white and blue roses to uniformed officers" style="left:36px;top:382px;width:332px;height:280px;background:linear-gradient(150deg,#6a5440 0%,#2b2a30 45%,#4b4e55 100%);"></div>
  </section>

  <svg class="support-shape" viewBox="0 0 1200 927" aria-hidden="true">
    <path d="M764 927 C 790 735, 905 570, 1012 568 C 1095 567, 1160 592, 1200 622 L1200 927 Z" fill="var(--navy)"/>
  </svg>

  <section class="support">
    <h2 class="support-title">Our support:</h2>
    <div class="support-rule"></div>
    <div class="body-copy" style="left:45px;top:682px;">
      <p>Activities that Harbor Lantern Fund<br>commonly supports:</p>
    </div>
    <ul class="bullet-list" style="left:67px;top:726px;">
      <li>Officer injury or illness</li>
      <li>HLF member/family injury or illness</li>
      <li>Officer death</li>
      <li>K9 death</li>
    </ul>
    <div class="body-copy" style="left:45px;top:839px;">
      <p>If you know of an officer in need, please<br>
      submit a request for support found on our<br>
      website at <span class="serif-strong">www.harborlanternfund.org</span></p>
    </div>
  </section>

</main>
</body>
</html>
```